依頼概要
■依頼の目的/概要
弊社が販売予定している玄米コーヒー(ドリップ式)のラベルデザインをお願いします。弊社は、森川緑風農園といいまして、自然農法栽培でお米や野菜を作っている農家です。信条は「土がきれいになれば世界が平和になる」です。今回の商品は健康食品としての位置づけになります。

■依頼詳細
今回は弊社が販売する玄米コーヒー(ドリップ式)のラベルのデザインをお願いします。
すでに、インスタント式の玄米コーヒーを販売しており、今回の商品はそれに続くプレミアム玄米コーヒーとして、前回よりも一段格上の商品を考えております。インスタント式は粉状ですが、今回の商品は粗挽きで本当の粗挽きコーヒーとほとんど変わらない色と形状です。入れた玄米コーヒーの色も、何も言わなければ本当のコーヒーと見分けがつきません。味もドリップ式はとっても美味しく、一度飲むと病みつきになります。

プレミアム玄米コーヒー(ドリップ式)の特徴は以下のとおりです。

●本当のコーヒーのようにドリップ式で美味しい玄米コーヒーが入れられます。
●使用している玄米は、自然農法栽培で作った、無肥料、無農薬のこだわりのお米を100%使用しています。
●コーヒーといっても、玄米飲料なのでノンカフェインで身体に優しいです。
●ポリフェノールや食物繊維が豊富に含まれていて、健康志向の人にはぴったりの飲料です。
●玄米には解毒作用があるようで、お通じが良くなり、身体の中をスッキリきれいにしてくれます。
(ちなみに初めて飲む方のなかには、下痢をされる方が多くいらっしゃいます。わたしもその一人でした。)
●内容量は200gです。

■その他の要望
●前回のインスタント式の商品の写真を添付してあります。前回は白のパッケージ(半透明、和紙風)でしたが、今回は濃い茶色(つや消し)のパッケージ(添付写真参照)になっており、高級感の漂うデザインが希望です。ドリップでコーヒーを入れている美しい写真をデザインにいれていただけると嬉しいです。(一目でドリップ式と分かる)
もちろん写真以外のデザインでも結構です。
●デザインの中に、森川緑風農園のロゴマークを入れてください。ファイルを添付してあります。
●パッケージの大きさは横140㎜×縦220㎜(190㎜)のチャック付スタンド袋です。

注意:表示法の関係で「自然農法」「無肥料」「無農薬」の言葉は使えません。
「自然栽培」「自然栽培法」「肥料不使用」「化学肥料不使用」「農薬不使用」の表記ならOKです。

その他何かご不明な点がございましたら、お気軽にご質問下さい。
デザイナーの皆様、どうぞよろしくお願いいたします!!
「ドリップ式」または「ドリップ用」という言葉をデザインの中に入れてください。
「プレミアム」という言葉も英語またはカタカナで入れてください。
■ 選んだ理由

私の希望通り、ドリップのシズル感と全体的な高級感がよく表現されていました。色の使い方が大変気に入りました。素晴らしいデザインを本当にありがとうございました。
とても満足しています。
また機会がありましたら、どうぞよろしくお願いいたします。

■ 提案者全員のお礼・コメント

この度は、たくさんの提案を頂きありがとうございました。
どれもすばらしいデザインばかりでした。
機会がありましたらまたよろしくお願いいたします。

```html
<!DOCTYPE html>
<html lang="ja">
<head>
<meta charset="UTF-8">
<title>玄米珈琲 PREMIUM ラベル</title>
<link href="https://fonts.googleapis.com/css2?family=Noto+Serif+JP:wght@400;600;700&family=Great+Vibes&family=Playfair+Display:wght@600&display=swap" rel="stylesheet">
<style>
  :root {
    --pouch: #6a4944;
    --pouch-dark: #5a3c38;
    --label: #1f1a18;
    --label-edge: #2b2421;
    --white: #f4f0ea;
    --muted: #cfc5b8;
    --photo-top: #3a2a22;
    --photo-mid: #8a6a52;
    --photo-low: #d8d0c6;
  }
  html, body {
    margin: 0;
    width: 867px;
    height: 1200px;
    overflow: hidden;
    background: var(--pouch);
  }
  .pouch {
    position: relative;
    width: 867px;
    height: 1200px;
    background: linear-gradient(180deg, var(--pouch) 0%, var(--pouch-dark) 100%);
  }
  .zipper {
    position: absolute;
    left: 0; right: 0; top: 120px;
    height: 2px;
    background: rgba(0,0,0,0.18);
  }
  .label {
    position: absolute;
    left: 130px;
    top: 300px;
    width: 607px;
    height: 740px;
    background: var(--label);
    box-shadow: inset 0 0 0 2px var(--label-edge);
    color: var(--white);
    font-family: "Noto Serif JP", serif;
    overflow: hidden;
  }
  .brand {
    position: absolute;
    left: 40px;
    top: 28px;
    display: flex;
    align-items: center;
    gap: 8px;
    font-size: 20px;
    font-weight: 600;
    letter-spacing: 3px;
    color: var(--muted);
  }
  .brand-dot {
    width: 10px; height: 10px; border-radius: 50%;
    background: var(--muted);
  }
  .title {
    position: absolute;
    left: 40px;
    top: 84px;
    margin: 0;
    font-size: 100px;
    font-weight: 600;
    letter-spacing: 12px;
    line-height: 1;
  }
  .subtitle {
    position: absolute;
    left: 190px;
    top: 196px;
    font-family: "Great Vibes", cursive;
    font-size: 34px;
    color: var(--muted);
  }
  .grade {
    position: absolute;
    left: 120px;
    top: 240px;
    font-family: "Playfair Display", serif;
    font-size: 54px;
    font-weight: 600;
    letter-spacing: 3px;
  }
  .claim {
    position: absolute;
    left: 300px;
    top: 318px;
    font-size: 17px;
    line-height: 1.55;
    letter-spacing: 1px;
    text-align: left;
  }
  .features {
    position: absolute;
    left: 40px;
    top: 392px;
    display: flex;
    gap: 22px;
    font-size: 15px;
    color: var(--muted);
    margin: 0; padding: 0;
    list-style: none;
  }
  .features li::before {
    content: "●";
    font-size: 10px;
    margin-right: 5px;
    vertical-align: 2px;
  }
  .features li:first-child::before { content: none; }
  .photo {
    position: absolute;
    left: 0;
    top: 430px;
    width: 607px;
    height: 310px;
    background: radial-gradient(ellipse at 40% 55%, var(--photo-low) 0%, var(--photo-mid) 35%, var(--photo-top) 80%);
  }
  .spec {
    position: absolute;
    right: 18px;
    bottom: 18px;
    text-align: right;
    font-size: 14px;
    line-height: 1.5;
    color: var(--white);
  }
</style>
</head>
<body>
  <div class="pouch">
    <div class="zipper"></div>
    <section class="label">
      <div class="brand"><span class="brand-dot"></span>FUSOU</div>
      <h1 class="title">玄米珈琲</h1>
      <div class="subtitle">Brown Rice Coffee</div>
      <div class="grade">PREMIUM</div>
      <p class="claim">農薬・化学肥料不使用で体に優しい！<br>“自然栽培玄米”100％使用</p>
      <ul class="features">
        <li>香味絶品</li>
        <li>香りとコク</li>
        <li>ノンカフェイン</li>
        <li>ポリフェノール</li>
      </ul>
      <div class="photo" role="img" aria-label="ドリッパーで玄米コーヒーを淹れている写真"></div>
      <div class="spec">ドリップ式<br>内容量200g</div>
    </section>
  </div>
</body>
</html>
```